Business card for auto dealership

Looking for a clean modern design.
Would like attached logo incorporated

Industry/Entity Type

Car dealership

Contact Information for Business Card

Name, website, phone, cell, fax, email

```html
<!DOCTYPE html>
<html lang="en">
<head>
<meta charset="utf-8">
<title>Harlow Truck &amp; Auto Sales — Business Card</title>
<link href="https://fonts.googleapis.com/css2?family=Montserrat:wght@400;700&display=swap" rel="stylesheet">
<style>
  :root {
    --backdrop: #4a4a4a;
    --card: #151515;
    --ink: #ffffff;
    --ink-soft: #e6e6e6;
  }
  * { margin: 0; padding: 0; box-sizing: border-box; }
  html, body { width: 1200px; height: 801px; overflow: hidden; }
  body {
    background: var(--backdrop);
    font-family: "Montserrat", sans-serif;
    color: var(--ink);
    display: flex;
    align-items: center;
    justify-content: center;
    gap: 40px;
  }
  .card {
    position: relative;
    width: 540px;
    height: 309px;
    background: var(--card);
    border-radius: 18px;
    overflow: hidden;
  }

  /* Front side */
  .name-tab {
    position: absolute;
    top: 22px;
    right: 0;
    width: 26px;
    height: 32px;
    background: var(--ink);
  }
  .holder {
    position: absolute;
    top: 20px;
    right: 40px;
    text-align: right;
  }
  .holder__name { font-weight: 700; font-size: 20px; letter-spacing: 0.5px; }
  .holder__title { font-weight: 400; font-size: 12px; color: var(--ink-soft); margin-top: 4px; letter-spacing: 0.5px; }

  .brand {
    font-weight: 700;
    color: var(--ink);
    line-height: 1;
  }
  .card--front .brand {
    position: absolute;
    left: 36px;
    top: 82px;
  }
  .brand__name { font-size: 40px; }
  .brand__line { font-size: 13px; letter-spacing: 1px; margin-top: 4px; }

  .contact {
    position: absolute;
    left: 36px;
    top: 158px;
    font-size: 12px;
    color: var(--ink-soft);
    list-style: none;
  }
  .contact__address { margin-bottom: 10px; line-height: 1.4; }
  .contact__item { display: flex; align-items: center; gap: 8px; margin-bottom: 4px; }
  .contact__item svg { width: 11px; height: 11px; fill: var(--ink); flex: none; }

  /* Back side */
  .card--back { display: flex; align-items: center; justify-content: center; }
  .card--back .brand { text-align: center; }
  .card--back .brand__name { font-size: 64px; }
  .card--back .brand__line { font-size: 20px; letter-spacing: 2px; margin-top: 8px; }
</style>
</head>
<body>

  <section class="card card--front" aria-label="Business card front">
    <div class="name-tab"></div>
    <div class="holder">
      <p class="holder__name">Dana Harlow</p>
      <p class="holder__title">Managing Director</p>
    </div>

    <div class="brand">
      <p class="brand__name">Harlow</p>
      <p class="brand__line">TRUCK &amp; AUTO SALES</p>
    </div>

    <ul class="contact">
      <li class="contact__address">Your address, City<br>State, Zip 1234</li>
      <li class="contact__item">
        <svg viewBox="0 0 24 24" aria-hidden="true"><path d="M6.6 10.8a15 15 0 0 0 6.6 6.6l2.2-2.2c.3-.3.7-.4 1-.2 1.1.4 2.3.6 3.6.6.6 0 1 .4 1 1V20c0 .6-.4 1-1 1A17 17 0 0 1 3 4c0-.6.4-1 1-1h3.5c.6 0 1 .4 1 1 0 1.3.2 2.5.6 3.6.1.3 0 .7-.2 1z"/></svg>
        555-210-4400
      </li>
      <li class="contact__item">
        <svg viewBox="0 0 24 24" aria-hidden="true"><path d="M7 1h10a2 2 0 0 1 2 2v18a2 2 0 0 1-2 2H7a2 2 0 0 1-2-2V3a2 2 0 0 1 2-2zm0 3v14h10V4z"/></svg>
        555-210-4471
      </li>
      <li class="contact__item">
        <svg viewBox="0 0 24 24" aria-hidden="true"><path d="M6 2h10l2 2v5h2a2 2 0 0 1 2 2v8a2 2 0 0 1-2 2H4a2 2 0 0 1-2-2v-8a2 2 0 0 1 2-2h2zm2 2v5h8V5l-1-1zm0 10v2h8v-2z"/></svg>
        555-210-4490
      </li>
      <li class="contact__item">
        <svg viewBox="0 0 24 24" aria-hidden="true"><path d="M2 5h20v14H2zm2 2v.5l8 5 8-5V7l-8 5z"/></svg>
        dana@harlowauto.com
      </li>
      <li class="contact__item">
        <svg viewBox="0 0 24 24" aria-hidden="true"><path d="M12 2a10 10 0 1 0 0 20 10 10 0 0 0 0-20zm0 2c1 0 2.3 2 2.8 5H9.2C9.7 6 11 4 12 4zM4.3 11h3c0 .7 0 1.4.1 2h-3a8 8 0 0 1 0-2zm5 0h5.4a16 16 0 0 1 0 2H9.3a16 16 0 0 1 0-2zm7.3 0h3a8 8 0 0 1 0 2h-3l.1-2zM12 20c-1 0-2.3-2-2.8-5h5.6c-.5 3-1.8 5-2.8 5z"/></svg>
        www.harlowauto.com
      </li>
    </ul>
  </section>

  <section class="card card--back" aria-label="Business card back">
    <div class="brand">
      <p class="brand__name">Harlow</p>
      <p class="brand__line">TRUCK &amp; AUTO SALES</p>
    </div>
  </section>

</body>
</html>
```